I am looking for a modern style design for a podcast cover art.
Titled: Open Horizon with R.T. Pellow
colors to stay in the grays, reds, blacks, white, gold, and maybe blues if it fits well. I attached a mock up of what we are going for and a current podcast cover we drew inspiration from.
Colors
3276b5
ec1f27
f04a50
1b1b1b
474747
919191
d2d2d2

```html
<!DOCTYPE html>
<html lang="en">
<head>
<meta charset="utf-8">
<title>Open Horizon with R.T. Pellow — Podcast Cover</title>
<link rel="stylesheet" href="https://fonts.googleapis.com/css2?family=Montserrat:wght@500;700&display=swap">
<style>
  :root {
    --page: #ffffff;
    --gold-deep: #6f501b;
    --gold-mid: #b8994f;
    --gold-light: #faf5cc;
    --title-light: #ffffff;
    --title-dark: #000000;
    --ink: #1b1b1b;
    --host-light: #474747;
    --host-dark: #1b1b1b;
  }
  html, body {
    margin: 0;
    padding: 0;
    width: 1200px;
    height: 1200px;
    overflow: hidden;
    background: var(--page);
  }
  .cover {
    display: block;
    width: 1200px;
    height: 1200px;
  }
  .byline {
    font-family: "Montserrat", Arial, sans-serif;
    font-size: 52px;
    fill: var(--ink);
    letter-spacing: 2px;
  }
  .byline-lead { font-weight: 500; }
  .byline-name { font-weight: 700; }
  .title {
    font-family: "Montserrat", Arial, sans-serif;
    font-weight: 700;
    font-size: 270px;
  }
  .title-top { fill: var(--title-light); }
  .title-bottom { fill: var(--title-dark); }
</style>
</head>
<body>
<svg class="cover" viewBox="0 0 1200 1200" xmlns="http://www.w3.org/2000/svg">
  <defs>
    <linearGradient id="gold-foil" x1="0" y1="0" x2="1" y2="1">
      <stop offset="0" stop-color="var(--gold-deep)"/>
      <stop offset="0.18" stop-color="var(--gold-deep)"/>
      <stop offset="0.42" stop-color="var(--gold-mid)"/>
      <stop offset="0.55" stop-color="var(--gold-light)"/>
      <stop offset="0.68" stop-color="var(--gold-mid)"/>
      <stop offset="0.85" stop-color="var(--gold-deep)"/>
      <stop offset="1" stop-color="var(--gold-deep)"/>
    </linearGradient>
    <linearGradient id="host-tone" x1="0" y1="0" x2="0" y2="1">
      <stop offset="0" stop-color="var(--host-light)"/>
      <stop offset="1" stop-color="var(--host-dark)"/>
    </linearGradient>
  </defs>

  <rect class="foil-panel" x="120" y="120" width="960" height="960" fill="url(#gold-foil)"/>

  <text class="byline" x="1024" y="270" text-anchor="end">
    <tspan class="byline-lead">WITH </tspan><tspan class="byline-name">R.T. PELLOW</tspan>
  </text>

  <text class="title title-top" x="176" y="546" textLength="850" lengthAdjust="spacingAndGlyphs">OPEN</text>
  <text class="title title-bottom" x="176" y="750" textLength="850" lengthAdjust="spacingAndGlyphs">HORIZON</text>

  <path class="host-photo" role="img"
    aria-label="Black and white photo of the host in a tuxedo, leaning and pointing upward"
    fill="url(#host-tone)"
    d="M258,1080 L258,830 Q270,778 330,772 L560,772 Q660,776 720,830 L890,1080 Z"/>
</svg>
</body>
</html>
```